Graphic Banner Design - 2.5' x 6' - High Tech Company

We are in need of a banner design for an outdoor sign that will be used at sponsorship events.

Size
2.5' x 6'

The company is a high tech company, and the design will be used for action sports events. So lining up to that would be good.

Tag line to be incorporated...
"Extreme IT Services for Extreme Needs."

Target Market(s)

Business Owners, Entrepreneurs, IT Professionals.

Industry/Entity Type

Information Technology

Logo Text

Vexlora

Colors

Designer to choose colors to be used in the design.

Requirements
Must have
• Must feel young and vibrant, fit in to an action sports event and just be out of this world awesome.
• In the world of the IT, we are the Zanverolli. Fast, Awesome, not necessarily cheap, but you know it will do what you want extremely well. Not for everyone, but always desired.

```html
<!DOCTYPE html>
<html lang="en">
<head>
<meta charset="utf-8">
<title>Vexlora Event Banner</title>
<link rel="stylesheet" href="https://fonts.googleapis.com/css2?family=Montserrat:wght@400&family=Open+Sans:wdth,wght@75..100,400;75..100,700&display=swap">
<style>
  :root {
    --backdrop: #bdbdbd;
    --charcoal: #454548;
    --panel-grey: #e6e7e9;
    --brand-blue: #2a5bd7;
    --ink: #3c3c3f;
    --white: #ffffff;
    --photo-deep: #2a2f52;
    --photo-mid: #6c77b8;
    --photo-glow: #dfe6ff;
  }
  html, body {
    margin: 0;
    width: 1200px;
    height: 800px;
    overflow: hidden;
    background: var(--backdrop);
  }
  .banner {
    position: absolute;
    left: 50px;
    top: 171px;
    width: 1300px;
    height: 540px;
    transform: scale(0.84615);
    transform-origin: top left;
    overflow: hidden;
  }
  .concert-photo {
    position: absolute;
    inset: 0;
    background:
      radial-gradient(ellipse 380px 260px at 450px 150px, var(--photo-glow) 0%, rgba(223,230,255,0.35) 45%, transparent 75%),
      radial-gradient(ellipse 300px 220px at 700px 200px, rgba(200,210,255,0.55) 0%, transparent 70%),
      linear-gradient(180deg, var(--photo-mid) 0%, var(--photo-deep) 55%, #3a3438 100%);
  }
  .shapes {
    position: absolute;
    inset: 0;
    width: 1300px;
    height: 540px;
  }
  .brand-name {
    position: absolute;
    left: 860px;
    width: 440px;
    top: 82px;
    margin: 0;
    text-align: center;
    font-family: "Montserrat", sans-serif;
    font-weight: 400;
    font-size: 46px;
    line-height: 1.2;
    color: var(--white);
  }
  .tagline {
    position: absolute;
    left: 880px;
    width: 355px;
    top: 180px;
    margin: 0;
    text-align: center;
    font-family: "Open Sans", sans-serif;
    font-stretch: 75%;
    font-weight: 700;
    font-size: 60px;
    line-height: 59px;
    color: var(--ink);
    text-transform: uppercase;
  }
  .tagline .accent { color: var(--brand-blue); }
  .web-address {
    position: absolute;
    left: 576px;
    top: 428px;
    height: 90px;
    display: flex;
    align-items: center;
    gap: 12px;
    font-family: "Open Sans", sans-serif;
    font-weight: 400;
    font-size: 50px;
    color: var(--white);
  }
  .web-address svg { width: 42px; height: 42px; }
</style>
</head>
<body>
  <div class="banner">
    <div class="concert-photo" role="img" aria-label="Photo of a crowd with raised hands at an outdoor concert, band on a stage under blue spotlights"></div>

    <svg class="shapes" viewBox="0 0 1300 540" aria-hidden="true">
      <polygon points="862,0 1300,0 1300,153 815,153" fill="var(--charcoal)"/>
      <polygon points="870,153 1300,153 1300,540 730,540" fill="var(--panel-grey)"/>
      <polygon points="856,153 870,153 730,540 716,540" fill="var(--brand-blue)"/>
      <polygon points="802,210 811,210 683,540 674,540" fill="var(--white)"/>
      <polygon points="820,230 826,230 708,540 702,540" fill="var(--charcoal)"/>
      <polygon points="575,428 1300,428 1300,518 545,518" fill="var(--brand-blue)"/>
    </svg>

    <h1 class="brand-name">Vexlora</h1>

    <p class="tagline">Extreme<br><span class="accent">IT Services</span><br>For Extreme<br>Needs</p>

    <div class="web-address">
      <svg viewBox="0 0 42 42" aria-hidden="true">
        <g fill="none" stroke="var(--white)" stroke-width="2">
          <circle cx="21" cy="21" r="18"/>
          <circle cx="21" cy="21" r="13"/>
          <ellipse cx="21" cy="21" rx="6" ry="13"/>
          <line x1="8" y1="21" x2="34" y2="21"/>
          <line x1="21" y1="8" x2="21" y2="34"/>
          <line x1="10" y1="15" x2="32" y2="15"/>
          <line x1="10" y1="27" x2="32" y2="27"/>
        </g>
      </svg>
      <span>www.vexlora.com</span>
    </div>
  </div>
</body>
</html>
```